Wedding Day Custom Wine Label - Tasmanian (Tamar Valley) wine

I am looking for a custom design that will be put on a wine label to commemorate a very good friend's wedding day.

We will need to be able to take the design and print it on to sticker labels that we can put on to wine bottles.

The bride and groom have asked for a simplistic label design (see example image attached). We need two labels. One for "Pinot Noir" wine and the other for "Chardonnay" wine. We would like the label to say:

The Hartwell's
Pinot Noir
2023
Tamar Valley

and for for the other wine variety:

The Hartwell's
Chardonnay
2023
Tamar Valley

smaller text below to say:

13.5% ALC/VOL 750ML
MEGAN & LIAM - 31.10.2024

I am happy to consider other variations - the bride & groom would prefer something minimalistic. Elegant and classy.

Target Market(s)

the bride & groom

Requirements
Must have
• Wedding date (31.10.2024). Wine type (Pinot Noir or Chardonnay).
Should not have
• images not essential

```html
<!DOCTYPE html>
<html lang="en">
<head>
<meta charset="utf-8">
<title>The Hartwell's – Wedding Wine Labels</title>
<link rel="stylesheet" href="https://fonts.googleapis.com/css2?family=Montserrat:wght@200;300;400&display=swap">
<style>
  :root {
    --page: #ffffff;
    --label-paper: #f8f0dc;
    --pinot-frame: #7f4a57;
    --chardonnay-frame: #d5cbb0;
    --inner-rule: #8b8088;
    --ink: #3a3236;
    --badge: #5b4b57;
    --badge-text: #efe6e8;
  }
  html, body {
    margin: 0;
    padding: 0;
    width: 1100px;
    height: 1200px;
    overflow: hidden;
    background: var(--page);
    font-family: "Montserrat", sans-serif;
    color: var(--ink);
  }
  .label-sheet {
    position: relative;
    width: 1100px;
    height: 1200px;
    display: flex;
    justify-content: center;
    align-items: center;
    gap: 40px;
  }
  .wine-label {
    position: relative;
    width: 500px;
    height: 640px;
    box-sizing: border-box;
    background: var(--label-paper);
    border: 7px solid var(--pinot-frame);
  }
  .wine-label--chardonnay { border-color: var(--chardonnay-frame); }
  .wine-label__inner-frame {
    position: absolute;
    inset: 14px;
    border: 1.5px solid var(--inner-rule);
  }
  .wine-label__name {
    position: absolute;
    top: 150px;
    left: 0;
    right: 0;
    text-align: center;
    font-weight: 200;
    font-size: 62px;
    letter-spacing: -2px;
    line-height: 1;
    margin: 0;
  }
  .wine-label__variety {
    position: absolute;
    top: 264px;
    left: 50%;
    transform: translateX(-50%);
    width: 224px;
    text-align: center;
    font-weight: 300;
    font-size: 37px;
    line-height: 1.2;
    padding-bottom: 2px;
    border-bottom: 1.5px solid var(--inner-rule);
    margin: 0;
  }
  .wine-label__details {
    position: absolute;
    top: 322px;
    left: 0;
    right: 0;
    text-align: center;
    font-weight: 400;
    font-size: 19px;
    letter-spacing: 1.5px;
    line-height: 25px;
  }
  .wine-label__couple {
    position: absolute;
    top: 410px;
    left: 50%;
    transform: translateX(-50%);
    width: 228px;
    height: 35px;
    border-radius: 4px;
    background: var(--badge);
    color: var(--badge-text);
    font-size: 13px;
    letter-spacing: 1px;
    display: flex;
    align-items: center;
    justify-content: center;
  }
  .wine-label__footer {
    position: absolute;
    left: 38px;
    right: 38px;
    top: 595px;
    display: flex;
    justify-content: space-between;
    font-size: 13px;
    letter-spacing: 0.5px;
  }
</style>
</head>
<body>
  <main class="label-sheet">
    <section class="wine-label wine-label--pinot">
      <div class="wine-label__inner-frame"></div>
      <h1 class="wine-label__name">The Hartwell's</h1>
      <h2 class="wine-label__variety">Pinot Noir</h2>
      <div class="wine-label__details">2023<br>TAMAR VALLEY</div>
      <div class="wine-label__couple">MEGAN &amp; LIAM - 31.10.2024</div>
      <div class="wine-label__footer"><span>13.5% ALC/VOL</span><span>750 ML</span></div>
    </section>
    <section class="wine-label wine-label--chardonnay">
      <div class="wine-label__inner-frame"></div>
      <h1 class="wine-label__name">The Hartwell's</h1>
      <h2 class="wine-label__variety">Chardonnay</h2>
      <div class="wine-label__details">2023<br>TAMAR VALLEY</div>
      <div class="wine-label__couple">MEGAN &amp; LIAM - 31.10.2024</div>
      <div class="wine-label__footer"><span>13.5% ALC/VOL</span><span>750 ML</span></div>
    </section>
  </main>
</body>
</html>
```